Plastic Aesthetic and Reconstructive Surgery

I need a double sided luxurius Business Card, with a minimal, modern design focused on my job.
Besides my Name, Surname and contact information, the use of my initials (M and T) in free style combination as a logo will help.
In the one side all data written in English.
In the other side written in Greek if possible.
Please feel free to use the letter type and size you prefer.
Please use icons type and size and orientation you like.
The Name, Surname, occupation and the initials can be UV spotted.
You can use also in the background a texture or something that will make the card luxurious.
I would prefer pal colors.
Each side can have different colors or even better they can be reversed or inverted
As I have said you can use the wet sand color, light brown, dark brown, gold, light gold, white
Updates

Need extra days to review

i am waiting for some new ideas and some modifications from the designers. I need a couple of days extention of the period for the designers to post their modifications.

Target Market(s)

Patients who need a reconstructive intervention or surgery. Also people, mainly women, that they need aesthetic or cosmetic interventions to face or body

Contact Information for Business Card

Name and surname, occupation, member of an organization , mobile telephone number, Mail, Pagebook and Snapgram accounts

Font styles to use
Script
Other font styles liked:
• Gabriola

Colors
FFC000
F8CF3A
FAE287
FDF2CF
FEFAEE

Requirements
Must have
• A free combination of my initials (M and T) as a logo
Nice to have
• Fade out with the background colors, UV spotted of the name, initials logo
Should not have
• Address

```html
<!DOCTYPE html>
<html lang="en">
<head>
<meta charset="utf-8">
<title>Markos Theodorou – Business Card</title>
<link href="https://fonts.googleapis.com/css2?family=Cinzel:wght@400&family=Alegreya+SC:wght@400&family=Cormorant+Garamond:wght@400;500&family=Tenor+Sans&display=swap" rel="stylesheet">
<style>
  :root {
    --backdrop: #5c4a3b;
    --sand: #a48c74;
    --tan: #a68d74;
    --ink: #111010;
    --paper: #ffffff;
  }
  * { margin: 0; padding: 0; box-sizing: border-box; }
  html, body { width: 1200px; height: 1000px; overflow: hidden; }
  body { background: var(--backdrop); position: relative; font-family: "Cormorant Garamond", serif; }

  .card {
    position: absolute; left: 294px; width: 613px; height: 351px;
    border-radius: 28px;
    box-shadow: 0 22px 40px rgba(30, 20, 12, 0.45);
  }
  .card--front { top: 124px; background: var(--sand); }
  .card--back { top: 552px; background: var(--paper); }

  .monogram {
    position: absolute; font-family: "Cormorant Garamond", serif; font-weight: 500;
    letter-spacing: -6px; line-height: 1;
  }
  .card--front .monogram { left: 0; right: 0; top: 78px; text-align: center; font-size: 112px; color: var(--ink); }
  .card--back .monogram { right: 34px; top: 86px; font-size: 84px; color: var(--tan); }

  .front-name {
    position: absolute; left: 0; right: 0; top: 226px; text-align: center;
    font-family: "Cinzel", serif; font-size: 22px; letter-spacing: 1px; color: var(--ink);
  }
  .front-role {
    position: absolute; left: 0; right: 0; top: 257px; text-align: center;
    font-family: "Tenor Sans", sans-serif; font-size: 11px; letter-spacing: 2.6px;
    text-transform: uppercase; color: var(--ink);
  }

  .back-name {
    position: absolute; left: 49px; top: 101px;
    font-family: "Alegreya SC", serif; font-size: 20px; letter-spacing: 1px; color: var(--ink);
  }
  .back-role, .back-member {
    position: absolute; left: 49px;
    font-family: "Alegreya SC", serif; font-size: 12.5px; letter-spacing: 1.6px; color: var(--ink);
  }
  .back-role { top: 128px; }
  .back-member { top: 166px; }

  .divider { position: absolute; left: 35px; right: 35px; top: 239px; height: 1px; background: var(--tan); }

  .contact {
    position: absolute; left: 47px; display: flex; align-items: center; gap: 11px;
    font-size: 17px; color: #222; font-weight: 500;
  }
  .contact svg { width: 18px; height: 18px; fill: var(--tan); }
  .contact--phone { top: 255px; }
  .contact--mail { top: 284px; }

  .social {
    position: absolute; right: 50px; top: 278px; display: flex; gap: 10px;
    font-family: "Cormorant Garamond", serif; font-weight: 500; font-size: 14px; color: var(--tan);
  }
</style>
</head>
<body>
  <section class="card card--front">
    <div class="monogram">MT</div>
    <h1 class="front-name">MARKOS THEODOROU, MD, MSC</h1>
    <p class="front-role">Plastic Reconstructive and Aesthetic Surgery</p>
  </section>

  <section class="card card--back">
    <h2 class="back-name">Μάρκος Θεοδώρου, MD, MSc</h2>
    <p class="back-role">Αισθητική και Επανορθωτική Πλαστική Χειρουργική</p>
    <p class="back-member">Μέλος Ε.Σ.Π.Α.Χ</p>
    <div class="monogram">MT</div>

    <div class="divider"></div>

    <p class="contact contact--phone">
      <svg viewBox="0 0 24 24" aria-hidden="true"><path d="M6.6 10.8a15.1 15.1 0 0 0 6.6 6.6l2.2-2.2c.3-.3.7-.4 1-.2 1.1.4 2.3.6 3.6.6.6 0 1 .4 1 1V20c0 .6-.4 1-1 1A17 17 0 0 1 3 4c0-.6.4-1 1-1h3.5c.6 0 1 .4 1 1 0 1.3.2 2.5.6 3.6.1.3 0 .7-.2 1z"/></svg>
      +30 690 000 1234
    </p>
    <p class="contact contact--mail">
      <svg viewBox="0 0 24 24" aria-hidden="true"><path d="M2 5h20v14H2zm2 2v.4l8 5.4 8-5.4V7zm0 2.8V17h16V9.8l-8 5.4z"/></svg>
      m.theodorou@example.com
    </p>

    <div class="social">
      <span>Pagebook</span>
      <span>Snapgram</span>
    </div>
  </section>
</body>
</html>
```